Sea Larq (www.sealarq.com) web site development

Sea Larq is a new Fishing, Spearfishing Charter operator offering private charters in North Belize, Turneffe, Lighthouse Reef and the Blue Hole. The logo of the company has been designed by Artflocker, some months ago. We have also developed a small brochure which can be the base for the website development (at least colors, fonts, etc.).
Pictures and Video should be an important asset of this website. We need to be able to update contents (video, photos), update prices and destinations, etc.

Target Market(s)

High hand, fishing and spearfishing enthusiasts.

Industry/Entity Type

Yacht charter

Coding

Coded - Design and coding required

Number of Pages Required

4 page

Colors
EB3D1F
EC4F4E
F09395
F8D3D4
FCEDEE

Requirements
Must have
• Optimized for phone and tablet navigation, must be easy to update with photos and video, connected to our Instagram and Facebook page,

```html
<!DOCTYPE html>
<html lang="en">
<head>
<meta charset="utf-8">
<title>Sea Larq — Private Fishing Charters</title>
<link rel="stylesheet" href="https://fonts.googleapis.com/css2?family=Exo+2:ital,wght@1,400;1,500;1,600;1,800&display=swap">
<style>
:root{
  --red-deep:#EB3D1F;
  --red:#EC4F4E;
  --rose:#F09395;
  --blush:#F8D3D4;
  --mist:#FCEDEE;
  --white:#ffffff;
}
*{margin:0;padding:0;box-sizing:border-box}
html,body{width:1200px;height:2856px;overflow:hidden}
body{
  position:relative;
  font-family:"Exo 2",sans-serif;font-style:italic;
  background:linear-gradient(180deg,var(--mist) 0,var(--mist) 1560px,#f6c3c4 1720px,var(--rose) 2100px,var(--red) 2480px,var(--red) 2856px);
}
.abs{position:absolute}
a{color:inherit}

/* hero */
.hero-band{left:0;top:0;width:845px;height:668px;background:var(--red)}
.contact-bar{left:845px;top:0;width:355px;height:33px;background:#f9dfe0;display:flex;align-items:center;justify-content:space-around;font-size:14px;color:var(--red-deep)}
.contact-bar span{display:flex;align-items:center;gap:6px}
.logo-tile{background:var(--mist);border-radius:0 0 12px 12px;display:flex;align-items:center;justify-content:center;gap:5px;color:var(--red-deep);font-weight:800;font-size:17px}
.logo-tile .dot{width:9px;height:9px;border-radius:50%;background:var(--red-deep)}
.logo-top{left:64px;top:0;width:100px;height:106px}
.main-nav{top:37px;left:0;width:845px;height:24px}
.main-nav a,.foot-nav a{position:absolute;text-decoration:none;color:var(--white);font-weight:600;font-size:17px;white-space:nowrap}
.main-nav a.current,.foot-nav a.current{color:var(--blush);border-bottom:1px solid var(--blush);padding-bottom:5px}
.hero-title{left:52px;top:160px;width:560px;font-weight:800;font-size:54px;line-height:61px;color:#f5b0b2}
.hero-sub{left:52px;top:370px;width:480px;font-size:18px;line-height:32px;color:var(--blush);font-weight:500}
.btn{left:52px;top:466px;width:166px;height:53px;border-radius:5px;background:var(--red-deep);color:var(--white);font-weight:600;font-size:18px;display:flex;align-items:center;justify-content:center}
.video{left:655px;top:175px;width:488px;height:350px;border-radius:14px;overflow:hidden;background:radial-gradient(ellipse 70% 45% at 55% 48%,#2b3547 0,#2f3f4f 60%,#3e6570 72%,#5a6660 82%,#4d5350 100%)}
.play{left:870px;top:324px;width:58px;height:50px;border-radius:9px;background:var(--red);display:flex;align-items:center;justify-content:center}
.photo{border-radius:6px}
.ph-fish{left:10px;top:594px;width:255px;height:183px;background:linear-gradient(180deg,#2e6fc4 0,#8db5e0 45%,#27528f 60%,#1e3f78 100%)}
.ph-spear{left:294px;top:594px;width:255px;height:183px;background:radial-gradient(circle at 55% 55%,#3b6f8b 0,#15324f 70%)}
.ph-snorkel{left:574px;top:594px;width:255px;height:183px;background:linear-gradient(180deg,#3fc6e6 0,#1ea6c8 55%,#4c8f60 85%,#3a6e42 100%)}
.deco{border-radius:50%;opacity:.55}

/* boat card */
.boat-card{left:149px;top:889px;width:1051px;height:727px;background:var(--white);border-radius:20px 0 0 20px}
.boat-heading{left:149px;top:924px;width:560px;height:151px;background:var(--blush);border-left:9px solid var(--red-deep);padding:16px 0 0 38px;font-weight:800;font-size:55px;line-height:67px;color:var(--rose)}
.boat-art{left:489px;top:898px;width:711px;height:710px}
.specs{left:191px;top:1134px;width:320px;list-style:none;color:var(--red-deep);font-size:18px;font-weight:600}
.specs li{height:39px}
.specs small{font-size:15px;font-weight:400}
.boat-note{left:191px;top:1453px;width:270px;font-size:18px;line-height:28.5px;color:var(--red-deep);font-weight:500}
.brand-block{left:680px;top:1508px;width:420px;text-align:center;color:var(--white)}
.brand-block h3{font-size:33px;font-weight:800;letter-spacing:11px}
.brand-block p{font-size:15px;line-height:27px;text-decoration:underline;font-weight:500}

/* adventure */
.adventure{left:65px;top:1788px;width:1070px;height:616px;border-radius:22px;background:rgba(236,140,142,.75)}
.adventure h2{position:absolute;left:0;top:36px;width:100%;text-align:center;font-weight:800;font-size:32px;color:var(--red-deep);letter-spacing:-.5px}
.copy{font-size:21px;line-height:32.5px;color:var(--white);font-weight:600}
.copy-left{left:88px;top:1902px;width:482px}
.copy-left p+p{margin-top:32px}
.copy-right{left:619px;top:1902px;width:492px}
.snap{border:4px solid var(--white);box-shadow:0 2px 5px rgba(0,0,0,.25)}
.snap-a{left:676px;top:2231px;width:102px;height:92px;background:linear-gradient(135deg,#1d6c8a,#0d3d5e);transform:rotate(-4deg)}
.snap-b{left:777px;top:2208px;width:126px;height:96px;background:linear-gradient(180deg,#6d8aa6,#2b4e70)}
.snap-c{left:752px;top:2301px;width:124px;height:95px;background:linear-gradient(180deg,#3aa0c7,#13698f);transform:rotate(-2deg)}
.logo-card{left:990px;top:2300px;width:100px;height:104px;border-radius:12px 12px 0 0}

/* footer */
.logo-foot{left:65px;top:2683px;width:117px;height:103px;border-radius:12px;font-size:19px}
.foot-nav{left:0;top:2717px;width:1200px;height:24px}
.copyright{left:0;top:2757px;width:1200px;text-align:center;color:var(--white);font-size:16px;font-weight:600}
.social{top:2715px;width:27px;height:27px;border-radius:50%;background:var(--white)}
</style>
</head>
<body>

<!-- hero -->
<div class="abs hero-band"></div>
<div class="abs contact-bar">
  <span>
    <svg width="17" height="12" viewBox="0 0 17 12" fill="none" stroke="#EB3D1F" stroke-width="1.3"><rect x=".7" y=".7" width="15.6" height="10.6" rx="1"/><path d="M1 1l7.5 6L16 1"/></svg>
    contact@sealarq.com
  </span>
  <span>
    <svg width="14" height="14" viewBox="0 0 24 24" fill="none" stroke="#EB3D1F" stroke-width="2"><path d="M22 16.9v3a2 2 0 0 1-2.2 2 19.8 19.8 0 0 1-8.6-3.1 19.5 19.5 0 0 1-6-6A19.8 19.8 0 0 1 2.1 4.2 2 2 0 0 1 4.1 2h3a2 2 0 0 1 2 1.7c.1 1 .4 1.9.7 2.8a2 2 0 0 1-.5 2.1L8 9.9a16 16 0 0 0 6 6l1.3-1.3a2 2 0 0 1 2.1-.4c.9.3 1.8.6 2.8.7a2 2 0 0 1 1.7 2z"/></svg>
    6004417
  </span>
</div>
<div class="abs logo-tile logo-top"><span class="dot"></span>Sea Larq</div>

<nav class="abs main-nav">
  <a class="current" style="left:268px">Home</a>
  <a style="left:344px">About&nbsp; Sea Larq</a>
  <a style="left:497px">Our Charters</a>
  <a style="left:627px">Contact Us</a>
</nav>

<h1 class="abs hero-title">Fishing, Spearfishing &amp; Snorkeling Private Charters</h1>
<p class="abs hero-sub">By helping each other we can spread more happiness to others join forces to build this happiness</p>
<div class="abs btn">Contact Us</div>

<div class="abs deco" role="img" aria-label="Illustration of a red charter boat" style="left:1018px;top:136px;width:126px;height:40px;background:var(--red);border-radius:40% 40% 10% 10%;opacity:.9"></div>
<div class="abs video" role="img" aria-label="Video thumbnail: aerial view of the Blue Hole"></div>
<div class="abs play"><svg width="22" height="24" viewBox="0 0 22 24"><path d="M2 2l18 10L2 22z" fill="#F8D3D4"/></svg></div>

<div class="abs photo ph-fish" role="img" aria-label="Photo: fishing rod bending over a fish at the ocean surface"></div>
<div class="abs photo ph-spear" role="img" aria-label="Photo: spearfisher underwater with a large tuna"></div>
<div class="abs photo ph-snorkel" role="img" aria-label="Photo: snorkelers over a coral reef"></div>

<div class="abs deco" role="img" aria-label="Illustration of a grey shark" style="left:1085px;top:595px;width:72px;height:60px;background:#a7b2b8"></div>
<div class="abs deco" role="img" aria-label="Illustration of two small fish" style="left:885px;top:692px;width:72px;height:50px;background:#b9c5c4"></div>

<!-- boat card -->
<div class="abs boat-card"></div>
<div class="abs boat-heading">OUR FISHING<br>MACHINE</div>
<svg class="abs boat-art" viewBox="0 0 711 710" role="img" aria-label="Photo: white sport fishing boat on the water">
  <defs>
    <linearGradient id="boatPhoto" x1="0" y1="0" x2="0" y2="1">
      <stop offset="0" stop-color="#4b78a8"/>
      <stop offset=".45" stop-color="#8eaed0"/>
      <stop offset=".62" stop-color="#d9dde2"/>
      <stop offset=".8" stop-color="#6d7b86"/>
      <stop offset="1" stop-color="#26384a"/>
    </linearGradient>
  </defs>
  <polygon points="201,0 711,0 711,710 0,710" fill="#EC4F4E"/>
  <polygon points="190,26 711,26 711,599 31,599" fill="url(#boatPhoto)"/>
</svg>
<ul class="abs specs">
  <li>Corvin 290 Open</li>
  <li>LFT <small>31'10" ;</small> Beam <small>11'6"</small></li>
  <li>Draft.: <small>2'0" ;</small> Weight.<small>10,000</small></li>
  <li>Fuel: <small>302 gals.</small></li>
  <li>Water <small>55 gals.</small></li>
  <li>Engines: <small>2 x 350hp Inboard</small></li>
  <li>Cruise Speed <small>20kn</small></li>
</ul>
<p class="abs boat-note">We outfit our boat with the latest electronics, up to date safety gear and finest equipment.</p>
<div class="abs brand-block">
  <h3>SEA LARQ</h3>
  <p>Palm Reach Lodge, Calle Marea,<br>Caye Corvo - Tel 6004417</p>
</div>

<div class="abs deco" role="img" aria-label="Illustration of a small fish" style="left:80px;top:1342px;width:48px;height:32px;background:#b9c5c4"></div>
<div class="abs deco" role="img" aria-label="Illustration of a swordfish" style="left:137px;top:1757px;width:136px;height:30px;background:#7fa3b2"></div>
<div class="abs deco" role="img" aria-label="Illustration of a swordfish" style="left:960px;top:1715px;width:136px;height:30px;background:#7fa3b2"></div>

<!-- adventure -->
<section class="abs adventure"><h2>JUST BRING YOUR APPETITE FOR ADVENTURE</h2></section>
<div class="abs copy copy-left">
  <p>We welcome both experienced fishermen/free divers and beginners. you can learn from our guides and even attend one of our introductory class to free dive and spearfishing from professional licensed instructors and expert scuba divers. you are welcome to take your gear with you, or leave us to provide you with all you need for an unforgettable experience. what you need to take with you is just your appetite for adventure.</p>
  <p>Sea Larq offers fishing , spearfishing and snorkeling private charters in north belize, turneffe, lighthouse reef and the blue hole.</p>
</div>
<p class="abs copy copy-right">No need to board crowded boats. Choose your privacy and let us pamper you with our exclusive service. Whether it is Snorkelling for the family, Tuna for the experienced angler, or Deep Sea Spearfishing for the fight of a lifetime, you will surely be pleased. Not only do we offer a vast assortment of trips but our local guides will coach you through each fight to ensure you catch your desired Trophy Fish.</p>
<div class="abs snap snap-a" role="img" aria-label="Photo: diver with a fish"></div>
<div class="abs snap snap-b" role="img" aria-label="Photo: fishing reels on a boat at sea"></div>
<div class="abs snap snap-c" role="img" aria-label="Photo: snorkeler in clear water"></div>
<div class="abs logo-tile logo-card"><span class="dot"></span>Sea Larq</div>

<div class="abs deco" role="img" aria-label="Illustration of a yellow fish" style="left:181px;top:2447px;width:46px;height:32px;background:#f6b73c;opacity:.9"></div>

<!-- footer -->
<div class="abs logo-tile logo-foot"><span class="dot"></span>Sea Larq</div>
<nav class="abs foot-nav">
  <a class="current" style="left:390px">Home</a>
  <a style="left:466px">About&nbsp; Sea Larq</a>
  <a style="left:619px">Our Charters</a>
  <a style="left:749px">Contact Us</a>
</nav>
<p class="abs copyright">Copyright &copy; 2021 - Sea Larq</p>
<div class="abs social" style="left:1010px" aria-label="Social profile one"></div>
<div class="abs social" style="left:1058px" aria-label="Social profile two"></div>
<div class="abs social" style="left:1107px" aria-label="Video channel"></div>
<div class="abs deco" role="img" aria-label="Illustration of an anglerfish" style="left:873px;top:2778px;width:74px;height:60px;background:#6f7f8c"></div>

</body>
</html>
```